**** Business card design for VoltaNode ****

For my ICT company VoltaNode I need I need a business card design.

We design, build and host web-applications and we have our own CMS product.

Some good examples are attached.

The information should be:
Joris Tielenburg
Managing director
E: j.tielenburg@voltanode-example.nl
M: +31(0)6 57218064
T: +31(0)40 7249305
W: www.voltanode-example.nl

Address:
Berend Vlootweg 27
5612 KT Eindhoven

Industry/Entity Type

Business

Requirements
Must have
• - Use logo (see attachments)
- Double sided
- Distinctive
Nice to have
• - Place for a statement on the back-side: "Crafted with insight, delivered with care"
- HTML code (or Wordpress)
- Dark (black or dark-gray) side
- Small simple images for telephone, e-mail en Url.
- QR code (only if not disturbing), not required, just an option

```html
<!DOCTYPE html>
<html lang="en">
<head>
<meta charset="utf-8">
<title>VoltaNode business card</title>
<link rel="stylesheet" href="https://fonts.googleapis.com/css2?family=PT+Sans:wght@400;700&display=swap">
<style>
  :root {
    --page: #e9e9eb;
    --card-dark: #05070d;
    --card-glow: #12305f;
    --brand-text: #c9d6dc;
    --brand-mark: #2f6fd6;
    --tagline: #9fe3e0;
    --ink-navy: #1f2a6b;
    --ink-dark: #1b1b1b;
    --card-light: #ffffff;
  }
  * { margin: 0; padding: 0; box-sizing: border-box; }
  html, body { width: 1200px; height: 900px; overflow: hidden; }
  body {
    background: var(--page);
    font-family: "PT Sans", Arial, sans-serif;
    position: relative;
  }
  .card {
    position: absolute;
    border-radius: 28px;
    overflow: hidden;
    box-shadow: 0 4px 14px rgba(0,0,0,0.25);
  }
  .card--front {
    left: 253px; top: 38px; width: 694px; height: 395px;
    background: radial-gradient(ellipse 55% 60% at 50% 50%, var(--card-glow) 0%, #0a1428 45%, var(--card-dark) 100%);
  }
  .card--back {
    left: 253px; top: 466px; width: 696px; height: 395px;
    background: var(--card-light);
  }
  .back__band {
    position: absolute; left: 0; top: 0; width: 100%; height: 120px;
    background: radial-gradient(ellipse 50% 120% at 50% 100%, #0f2448 0%, var(--card-dark) 80%);
  }
  .brand { position: absolute; display: flex; align-items: center; }
  .brand__dot {
    border-radius: 50%;
    background: var(--brand-mark);
    flex: none;
  }
  .brand__name {
    color: var(--brand-text);
    font-weight: 400;
    line-height: 1;
    white-space: nowrap;
  }
  .card--front .brand { left: 60px; top: 150px; }
  .card--front .brand__dot { width: 110px; height: 110px; margin-right: 58px; }
  .card--front .brand__name { font-size: 84px; letter-spacing: 3px; }
  .tagline {
    position: absolute; left: 0; right: 0; top: 288px;
    text-align: center;
    color: var(--tagline);
    font-size: 24px;
    letter-spacing: 1.2px;
  }
  .card--back .brand { left: 80px; top: 47px; }
  .card--back .brand__dot { width: 80px; height: 80px; margin-right: 45px; }
  .card--back .brand__name { font-size: 44px; letter-spacing: 2px; }
  .person { position: absolute; left: 119px; top: 168px; }
  .person__name { color: var(--ink-navy); font-weight: 700; font-size: 36px; line-height: 1.05; }
  .person__role { color: var(--ink-dark); font-size: 22px; letter-spacing: 0.5px; line-height: 1.15; }
  .contact {
    position: absolute;
    display: flex; align-items: flex-start;
    color: var(--ink-navy);
    font-size: 16px; line-height: 26px;
    white-space: nowrap;
  }
  .contact svg { flex: none; margin-right: 10px; }
  .contact--address { left: 78px; top: 266px; }
  .contact--email   { left: 80px; top: 338px; font-size: 15px; }
  .contact--phone   { left: 377px; top: 267px; }
  .contact--mobile  { left: 377px; top: 303px; }
  .contact--web     { left: 377px; top: 339px; }
</style>
</head>
<body>
  <section class="card card--front">
    <div class="brand">
      <span class="brand__dot"></span>
      <span class="brand__name">VoltaNode</span>
    </div>
    <p class="tagline">Crafted with insight, delivered with care</p>
  </section>

  <section class="card card--back">
    <div class="back__band"></div>
    <div class="brand">
      <span class="brand__dot"></span>
      <span class="brand__name">VoltaNode</span>
    </div>

    <div class="person">
      <h1 class="person__name">Joris Tielenburg</h1>
      <p class="person__role">Managing&nbsp; Director</p>
    </div>

    <div class="contact contact--address">
      <svg width="28" height="26" viewBox="0 0 28 26" aria-hidden="true">
        <path d="M14 2 L2 13 H6 V24 H12 V17 H16 V24 H22 V13 H26 Z" fill="#111"/>
      </svg>
      <p>Berend Vlootweg 27<br>5612 KT Eindhoven</p>
    </div>

    <div class="contact contact--email">
      <svg width="26" height="24" viewBox="0 0 26 24" aria-hidden="true">
        <rect x="1.5" y="4" width="23" height="16" fill="none" stroke="#111" stroke-width="1.8"/>
        <path d="M1.5 4 L13 14 L24.5 4" fill="none" stroke="#111" stroke-width="1.8"/>
      </svg>
      <p>j.tielenburg@voltanode-example.nl</p>
    </div>

    <div class="contact contact--phone">
      <svg width="26" height="26" viewBox="0 0 26 26" aria-hidden="true">
        <circle cx="13" cy="13" r="11.5" fill="none" stroke="#111" stroke-width="1.8"/>
        <path d="M9 7 L11 7 L12 10 L10.5 11.5 Q12 14.5 14.5 15.5 L16 14 L19 15 L19 17 Q17 19.5 13 17 Q8.5 14 7.5 10 Q7.5 8 9 7 Z" fill="#111"/>
      </svg>
      <p>+31(0)40 7249305</p>
    </div>

    <div class="contact contact--mobile">
      <svg width="26" height="26" viewBox="0 0 26 26" aria-hidden="true">
        <circle cx="13" cy="13" r="11.5" fill="none" stroke="#111" stroke-width="1.8"/>
        <rect x="9.5" y="6" width="7" height="14" rx="1.5" fill="none" stroke="#111" stroke-width="1.6"/>
        <line x1="11.5" y1="17.5" x2="14.5" y2="17.5" stroke="#111" stroke-width="1.2"/>
      </svg>
      <p>+31(0)6 57218064</p>
    </div>

    <div class="contact contact--web">
      <svg width="26" height="26" viewBox="0 0 26 26" aria-hidden="true">
        <circle cx="13" cy="13" r="11" fill="none" stroke="#111" stroke-width="1.6"/>
        <ellipse cx="13" cy="13" rx="5" ry="11" fill="none" stroke="#111" stroke-width="1.4"/>
        <line x1="2" y1="13" x2="24" y2="13" stroke="#111" stroke-width="1.4"/>
        <line x1="4" y1="7.5" x2="22" y2="7.5" stroke="#111" stroke-width="1.2"/>
        <line x1="4" y1="18.5" x2="22" y2="18.5" stroke="#111" stroke-width="1.2"/>
      </svg>
      <p>www.voltanode-example.nl</p>
    </div>
  </section>
</body>
</html>
```